Two sided DL flyer for promotional event

I had a full web design and logo done through craftloop a year or so ago and now require some promotional materials.

I will have the text attached for a flyer soon, please use Lorem Ipsum for the moment (approx two paragraphs) and want it to be in a similar style to the website, and using the current logo and colour schemes. I like the way the website break sections, with the arc, I'd like to use that.

(as per attachments)
Front side - Velmora Digital Logo, Bullet Points of Services, Brand Catch Phrase
Back Side - Logos of Partners, Two Paragraphs of Text (TBC, use Lorem Ipsum), Testimonial (pick one from the website)

Be aware that the new design on the website is not fully completed yet so there are typos etc, but you will get the idea of style.

www.velmoradigital.com/velmoranewdesign

Target Market(s)

accountants, financial planners, consultants, small business owners

Industry/Entity Type

Digital

Font styles to use
Serif
Sans Serif
Other font styles liked:
• Harabara (attached), or if this isn't appropriate for paragraph text, Ubuntu or Candara

Requirements
Must have
• current logo, only colours from guidelines (attached), sections and copy as per attachments

```html
<!DOCTYPE html>
<html lang="en">
<head>
<meta charset="utf-8">
<title>Velmora Digital – DL Flyer</title>
<link rel="stylesheet" href="https://fonts.googleapis.com/css2?family=Source+Sans+3:wght@400;600;700&family=PT+Sans+Narrow:wght@400;700&family=Varela+Round&display=swap">
<style>
:root{
  --stage:#4a3929;
  --paper:#ffffff;
  --mist:#e6e8ea;
  --navy:#0d4464;
  --blue:#1a6389;
  --teal:#1f6f93;
  --orange:#ef7f32;
  --orange-soft:#f39a4d;
  --red:#a3171e;
  --red-bright:#d9372a;
  --ink:#2b2b2b;
  --pale-blue:#b9d7e6;
  --social:#2d6fb7;
}
*{box-sizing:border-box;margin:0;padding:0}
html,body{width:1200px;height:854px;overflow:hidden}
body{background:var(--stage);font-family:"Source Sans 3",Arial,sans-serif;position:relative}
.flyer{position:absolute;top:90px;width:487px;height:690px;background:var(--paper);overflow:hidden;box-shadow:0 4px 14px rgba(0,0,0,.45)}
.flyer--back{left:80px}
.flyer--front{left:603px}
.shape{position:absolute;left:0;top:0;width:487px;height:690px}
.abs{position:absolute}
.center{left:0;width:100%;text-align:center}

/* back */
.intro{top:14px;left:30px;width:427px;text-align:center;color:var(--teal);font-weight:700;font-size:14.5px;line-height:18px}
.col-title{color:var(--orange);font-weight:700;font-size:16px;line-height:20px}
.col-text{color:#fff;font-size:10.2px;line-height:11.8px;text-align:justify}
.contact-line{top:318px;color:#fff;font-size:18px;font-weight:400}
.contact-line b{font-weight:700}
.rounded-tag{font-family:"Varela Round",Arial,sans-serif;color:#fff;font-weight:700;letter-spacing:.6px}
.testi-head{top:394px;color:#fff;font-size:13px;font-weight:700}
.testi-head span{font-weight:400;opacity:.85}
.testi-quote{top:424px;left:22px;width:443px;color:#fff;font-size:6.7px;line-height:8.5px}
.testi-name{right:22px;top:462px;color:#fff;font-size:8px;font-weight:700;text-align:right}
.testi-org{right:22px;top:473px;color:#fff;font-size:6px;text-align:right}
.partner{position:absolute;background:var(--mist)}
.site{top:638px;color:var(--red);font-weight:700;font-size:17px}
.chat{top:668px;color:#fff;font-size:11px}
.chat b{font-weight:700}

/* front */
.brand{left:30px;top:28px;display:flex;align-items:center;gap:8px}
.brand-mark{width:36px;height:36px;border-radius:50%;background:var(--teal)}
.brand-name{font-size:26px;color:var(--teal);font-weight:600}
.social{position:absolute;top:30px;width:28px;height:28px;border-radius:50%;background:var(--social)}
.front-title{top:100px;font-family:"Varela Round",Arial,sans-serif;font-size:22px;color:#fff;letter-spacing:1px}
.front-sub{top:131px;font-size:20px;color:var(--orange-soft);font-weight:600}
.photo{position:absolute;border-radius:50%}
.banner{position:absolute;left:0;height:22px;width:210px;color:#fff;font-family:"PT Sans Narrow",Arial,sans-serif;font-weight:700;font-size:14px;line-height:22px;padding-left:32px;background:linear-gradient(90deg,var(--red),var(--red-bright));clip-path:polygon(0 0,200px 0,210px 50%,200px 100%,0 100%)}
.section-title{color:var(--teal);font-weight:600;font-size:16.5px;line-height:19px}
.services{position:absolute;left:30px;top:457px;width:195px;list-style:none}
.services li{position:relative;height:17.1px;padding-left:16px;font-size:9.2px;line-height:14px;color:var(--ink);border-bottom:1px solid var(--pale-blue)}
.services li::before{content:"";position:absolute;left:2px;top:4px;width:6px;height:6px;border-radius:50%;background:var(--red)}
.pm-text{left:250px;top:360px;width:206px;color:var(--ink);font-size:10.2px;line-height:11.8px;text-align:justify}
.contact-block{right:31px;text-align:right;color:var(--ink)}
.contact-title{top:525px;color:var(--orange);font-size:13px}
.contact-addr{top:543px;font-size:10px;line-height:14px}
.tel{top:580px;color:var(--navy);font-size:24px;font-weight:400}
.tel b{font-weight:700}
</style>
</head>
<body>

<section class="flyer flyer--back" aria-label="Flyer back">
  <svg class="shape" viewBox="0 0 487 690" aria-hidden="true">
    <defs>
      <linearGradient id="topFade" x1="0" y1="0" x2="0" y2="1"><stop offset="0" stop-color="#f4f5f6"/><stop offset="1" stop-color="#dfe2e5"/></linearGradient>
      <linearGradient id="navyFill" x1="0" y1="0" x2="0" y2="1"><stop offset="0" stop-color="#1a6389"/><stop offset="1" stop-color="#0d4464"/></linearGradient>
    </defs>
    <rect width="487" height="100" fill="url(#topFade)"/>
    <path d="M0 98 Q120 78 228 80 Q236 80 240 88 Q243 80 250 80 Q360 78 487 98 L487 400 L0 400 Z" fill="url(#navyFill)"/>
    <path d="M0 392 Q120 386 228 386 Q236 386 243 378 Q250 386 258 386 Q370 386 487 392 L487 492 Q243 478 0 492 Z" fill="var(--orange)"/>
    <path d="M0 672 Q243 630 487 672 L487 690 L0 690 Z" fill="var(--mist)"/>
    <path d="M0 676 Q243 648 487 676 L487 690 L0 690 Z" fill="var(--navy)"/>
  </svg>

  <p class="abs intro">Our clients choose Velmora Digital because our depth of experience and our unrelenting commitment to solving the most challenging business problems.</p>

  <h2 class="abs col-title" style="left:28px;top:108px;width:200px">Lorem ipsum dolor sit amet dolor sit amet</h2>
  <p class="abs col-text" style="left:28px;top:158px;width:198px">Lorem ipsum dolor sit amet, consectetur adipisicing elit, sed do eiusmod tempor incididunt ut labore et dolore magna aliqua. Ut enim ad minim veniam, quis nostrud exercitation ullamco laboris nisi ut aliquip ex ea commodo consequat. Duis aute irure dolor in reprehenderit in voluptate velit esse cillum dolore eu fugiat nulla pariatur. Excepteur sint occaecat cupidatat non proident, sunt in culpa qui officia deserunt mollit anim id est laborum.</p>

  <h2 class="abs col-title" style="left:256px;top:108px;width:200px">Lorem ipsum dolor sit amet</h2>
  <p class="abs col-text" style="left:256px;top:138px;width:198px">Lorem ipsum dolor sit amet, consectetur adipisicing elit, sed do eiusmod tempor incididunt ut labore et dolore magna aliqua. Ut enim ad minim veniam, quis nostrud exercitation ullamco laboris nisi ut aliquip ex ea commodo consequat. Duis aute irure dolor in reprehenderit in voluptate velit esse cillum dolore eu fugiat nulla pariatur. Excepteur sint occaecat cupidatat non proident, sunt in culpa qui officia deserunt mollit anim id est laborum.</p>

  <p class="abs center contact-line">Contact Us: <b>(03) 9000 4411</b></p>
  <p class="abs center rounded-tag" style="top:346px;font-size:14px">nonummy nibh euismod</p>

  <p class="abs center testi-head">Testimonials <span>/ WHAT OUR CLIENTS SAY</span></p>
  <p class="abs testi-quote">“Recently I had the pleasure of engaging and working closely on an I.T systems implantation project with Theo from Velmora and was very pleased with the results. Theo's knowledge, professionalism and courteous manner greatly assisted and expedited a successful knowledge transfer to our staff that was absolutely essential to the overall success of the project. I highly recommend both Theo and Velmora if you are truly focused on achieving real results.”</p>
  <p class="abs testi-name">Mara Keller</p>
  <p class="abs testi-org">Brightline</p>

  <div class="partner" role="img" aria-label="Partner badge" style="left:40px;top:506px;width:170px;height:34px;border-radius:3px"></div>
  <div class="partner" role="img" aria-label="Partner badge" style="left:237px;top:509px;width:212px;height:28px;border-radius:3px"></div>
  <div class="partner" role="img" aria-label="Partner badge" style="left:96px;top:561px;width:94px;height:52px;border-radius:8px"></div>
  <div class="partner" role="img" aria-label="Partner badge" style="left:211px;top:552px;width:72px;height:72px;border-radius:50%"></div>
  <div class="partner" role="img" aria-label="Partner badge" style="left:310px;top:564px;width:112px;height:46px;border-radius:3px"></div>

  <p class="abs center site">velmoradigital.com</p>
  <p class="abs center chat">Chatly: <b>theo.velmoradigital</b></p>
</section>

<section class="flyer flyer--front" aria-label="Flyer front">
  <svg class="shape" viewBox="0 0 487 690" aria-hidden="true">
    <defs>
      <linearGradient id="topFadeF" x1="0" y1="0" x2="0" y2="1"><stop offset="0" stop-color="#f6f7f8"/><stop offset="1" stop-color="#dfe2e5"/></linearGradient>
      <linearGradient id="navyFillF" x1="0" y1="0" x2="0" y2="1"><stop offset="0" stop-color="#1a6389"/><stop offset="1" stop-color="#124f72"/></linearGradient>
    </defs>
    <rect width="487" height="100" fill="url(#topFadeF)"/>
    <path d="M0 98 Q120 78 228 80 Q236 80 240 88 Q243 80 250 80 Q360 78 487 98 L487 262 Q300 262 200 285 Q100 305 0 300 Z" fill="url(#navyFillF)"/>
    <circle cx="236" cy="296" r="9" fill="var(--pale-blue)"/>
    <circle cx="258" cy="300" r="8" fill="var(--pale-blue)"/>
    <circle cx="281" cy="308" r="12" fill="var(--pale-blue)"/>
    <circle cx="305" cy="299" r="7" fill="var(--pale-blue)"/>
    <path d="M0 672 Q243 630 487 672 L487 690 L0 690 Z" fill="var(--mist)"/>
    <path d="M0 676 Q243 648 487 676 L487 690 L0 690 Z" fill="var(--navy)"/>
  </svg>

  <div class="abs brand">
    <span class="brand-mark"></span>
    <span class="brand-name">VelmoraDigital</span>
  </div>
  <span class="social" style="left:358px"></span>
  <span class="social" style="left:392px"></span>
  <span class="social" style="left:426px"></span>

  <h1 class="abs center front-title">nonummy nibh euismod</h1>
  <p class="abs center front-sub">Solving the most challenging business problems</p>

  <div class="photo" role="img" aria-label="Photo of laptop, tablet and phone showing software dashboards" style="left:76px;top:195px;width:120px;height:82px;border:3px solid #fff;outline:2px solid var(--orange);background:radial-gradient(circle,#e8edf1,#aebcc7)"></div>
  <div class="photo" role="img" aria-label="Photo of a hand holding a smartphone beside a coffee cup" style="left:197px;top:166px;width:150px;height:128px;border:4px solid #fff;outline:3px solid var(--orange);background:radial-gradient(circle at 60% 45%,#c9d3db,#4a5158)"></div>

  <div class="banner" style="top:308px">Technical, Yet Approachable</div>
  <div class="banner" style="top:337px">Professional, Yet Personable</div>
  <div class="banner" style="top:366px">Casual, Yet Dependable</div>

  <h2 class="abs section-title" style="left:30px;top:411px">Software Training<br>and Implementation</h2>
  <ul class="services">
    <li>Ledgra Training and Implementation</li>
    <li>Fieldpro Training and Implementation</li>
    <li>Taskflow Pro Training and Implementation</li>
    <li>Routely Training and Implementation</li>
    <li>Cloudsuite Apps-Training and Implementation</li>
    <li>Mailpost to Cloudsuite Apps</li>
    <li>Demystifying Cloud Software</li>
    <li>Stockwise Training and Implementation</li>
    <li>Slotly Implementation and Training</li>
    <li>Tillpoint Training and Implementation</li>
  </ul>

  <h2 class="abs section-title" style="left:277px;top:330px">Project Management</h2>
  <p class="abs pm-text">Lorem ipsum dolor sit amet, consectetur adipisicing elit, sed do eiusmod tempor incididunt ut labore et dolore magna aliqua. Ut enim ad minim veniam, quis nostrud exercitation ullamco laboris nisi ut aliquip ex ea commodo consequat. Duis aute irure dolor in reprehenderit in voluptate velit esse cillum dolore eu fugiat nulla pariatur. Excepteur sint occaecat cupidatat non proident, sunt in culpa qui officia deserunt mollit anim id est laborum.</p>

  <p class="abs contact-block contact-title">Contact us</p>
  <p class="abs contact-block contact-addr">Level 4, 12 Harbour Lane, Melbourne, VIC<br>Email: info@velmoradigital.com.au</p>
  <p class="abs contact-block tel">Tel: <b>(03) 9000 4411</b></p>

  <p class="abs center site">velmoradigital.com</p>
  <p class="abs center chat">Chatly: <b>theo.velmoradigital</b></p>
</section>

</body>
</html>
```